Dental Design, very professional and noticable

Tindale Ridge Dental Surgery is based in Pelican Waters. We are a fast growing dental surgery and are looking for some professional business cards to send to patients.
We would like to see a design that is Vertical and uses the colours Soft Blue, Silver, White and Black. Maybe a full blue side with moto and details on back? Any other ideas or colours that you may think will make the card look unique is fine.
We need all details on the card that are listed above

Target Market(s)

Families, Retired, Other Professionals and Businesses

Industry/Entity Type

Dental

Contact Information for Business Card

Tindale Ridge Dental Surgery
Family, Cosmetic, Preventative
Dr. Owen Castrey
Dental Surgeon
BDS (Adel) FAE FADI FICD FPFA
phone: (07)50001846
fax: (07)50002917
email: tindaleridgedental@quillpost.com
http://tindaleridgedental.com/

Logo Text

Logo styles of interest
Abstract Logo
Requirements
Must have
• Vertical, Vibrant but Professional, Rounded Edges, Logo on front and back of card (different colours on each side)
Nice to have
• One side completely blue (not sure what shade) with logo and moto on bottom
Other side white, with blue or different coloured logo with details in black and silver?
Logo should show half circle with 1 end as arrow symbolizing pelican waters canal also a magnifine glass also half circled with 1 end as arrow. Any other ideas are welcome.
Should not have
• A tooth. A smile. Toothbrush or Toothpaste. Cornered edges.

```html
<!DOCTYPE html>
<html lang="en">
<head>
<meta charset="utf-8">
<title>Tindale Ridge Dental Surgery – Business Cards</title>
<link rel="stylesheet" href="https://fonts.googleapis.com/css2?family=Noto+Serif+Display:wght@400&family=Open+Sans:wght@400&family=Archivo+Narrow:wght@400&display=swap">
<style>
  :root {
    --backdrop: #ece7df;
    --card-blue: #283a8f;
    --card-white: #ffffff;
    --gold: #977f32;
    --gold-light: #a88f38;
    --sky: #1ea6e3;
    --mark-blue: #1b79c0;
    --ink: #111111;
    --silver: #7d7f86;
  }
  * { margin: 0; padding: 0; box-sizing: border-box; }
  html, body {
    width: 1200px; height: 1200px; overflow: hidden;
    background: var(--backdrop);
  }
  .canvas { position: relative; width: 1200px; height: 1200px; }
  .card {
    position: absolute; width: 516px; height: 880px;
    border-radius: 28px; overflow: hidden;
    box-shadow: 0 6px 18px rgba(0,0,0,.18);
  }
  .card--front { left: 100px; top: 230px; background: var(--card-blue); }
  .card--back  { left: 660px; top: 170px; background: var(--card-white); }

  .serif {
    font-family: "Noto Serif Display", "Times New Roman", serif;
    font-weight: 400;
    white-space: nowrap;
    line-height: 1.1;
  }
  /* condensed serif lines: centred then narrowed horizontally */
  .narrow {
    position: absolute; left: 50%;
    transform: translateX(-50%) scaleX(var(--sx, .62));
    transform-origin: center top;
  }
  .narrow--left {
    left: var(--x, 40px);
    transform: scaleX(var(--sx, .62));
    transform-origin: left top;
  }

  .brand {
    position: absolute; left: 0; right: 0;
    display: flex; align-items: center; justify-content: center; gap: 18px;
  }
  .brand__dot { width: 64px; height: 64px; border-radius: 50%; flex: none; }
  .brand__name { font-size: 54px; }

  .card--front .brand { top: 190px; }
  .card--front .brand__dot { background: var(--gold); }
  .card--front .brand__name { color: var(--gold); }

  .card--back .brand { top: 70px; }
  .card--back .brand__dot { background: var(--mark-blue); }
  .card--back .brand__name { color: var(--mark-blue); }

  .card--front .title { top: 410px; font-size: 50px; color: var(--gold); --sx: .66; }
  .card--front .motto { top: 475px; font-size: 46px; color: var(--gold-light); --sx: .64; }
  .doctor { top: 660px; font-size: 50px; color: var(--sky); --sx: .57; }
  .credentials { top: 748px; font-size: 32px; color: var(--sky); letter-spacing: 2px; word-spacing: 6px; --sx: .64; }

  .card--back .title { top: 170px; font-size: 52px; color: var(--ink); --x: 32px; --sx: .6; }
  .card--back .motto { top: 234px; font-size: 48px; color: var(--silver); --x: 44px; --sx: .58; }

  .contact { position: absolute; left: 44px; white-space: nowrap; }
  .contact--phone {
    top: 380px; font-family: "Open Sans", Arial, sans-serif;
    font-size: 32px; line-height: 48px; color: var(--silver); letter-spacing: 1px;
  }
  .contact--web {
    top: 510px; left: 26px; font-family: "Archivo Narrow", "Arial Narrow", sans-serif;
    font-size: 29px; line-height: 46px; color: var(--ink);
  }
</style>
</head>
<body>
<main class="canvas">
  <section class="card card--front" aria-label="Front of card">
    <div class="brand">
      <span class="brand__dot"></span>
      <span class="brand__name serif">Tindale Ridge</span>
    </div>
    <h1 class="title serif narrow">Tindale Ridge Dental Surgery</h1>
    <p class="motto serif narrow">Family, Cosmetics, Preventive</p>
    <p class="doctor serif narrow">Dr. Owen Castrey , Dental Surgeon</p>
    <p class="credentials serif narrow">DBS (Adel) FAE FADI FICD FPFA</p>
  </section>

  <section class="card card--back" aria-label="Back of card">
    <div class="brand">
      <span class="brand__dot"></span>
      <span class="brand__name serif">Tindale Ridge</span>
    </div>
    <h2 class="title serif narrow narrow--left">Tindale Ridge Dental Surgery</h2>
    <p class="motto serif narrow narrow--left">Family, Cosmetics, Preventive</p>
    <p class="contact contact--phone">Phone:(07)50001846<br>Fax:(07)50002917</p>
    <p class="contact contact--web">Email:tindaleridgedental@quillpost.com<br>http://tindaleridgedental.com</p>
  </section>
</main>
</body>
</html>
```